Marta Quinlan Photography needs a unique, creative business card/logo design

I need a design for business cards/logo that is unique and creative in the industry. Simplicity is nice, so not too crowded. Something that will catch my customer's eye and remain in their memory. I am primarily a landscape photographer but will be soon may be branching into boudoir photography as well. I have attached my current card.

Industry/Entity Type

Business

Contact Information for Business Card

Marta Quinlan Photography
Phone: 0439 271 504
Email: MartaQuinlanPhotography@brivomail.net
Website: www.pagerly.net/MartaQuinlanPhotography.Aust

Logo Text

Marta Quinlan Photography

Requirements
Must have
• Contact Details on one side
Should not have
• pixelation

```html
<!DOCTYPE html>
<html lang="en">
<head>
<meta charset="UTF-8">
<title>Marta Quinlan Photography – Business Card</title>
<link href="https://fonts.googleapis.com/css2?family=Roboto:wght@400;500;700&display=swap" rel="stylesheet">
<style>
  :root {
    --backdrop: #d6d6d6;
    --card: #ffffff;
    --mint: #8fcfc6;
    --ink: #1c1c1c;
    --rule: #3a3a3a;
    --band: #222222;
    --band-text: #ffffff;
  }
  * { margin: 0; padding: 0; box-sizing: border-box; }
  html, body {
    width: 1200px;
    height: 800px;
    overflow: hidden;
    background: var(--backdrop);
  }
  .canvas {
    position: relative;
    width: 1200px;
    height: 800px;
  }
  .card {
    position: absolute;
    top: 272px;
    width: 473px;
    height: 263px;
    background: var(--card);
    overflow: hidden;
  }
  .card--front { left: 61px; }
  .card--back { left: 641px; }

  /* Front: brand name */
  .brand {
    position: absolute;
    inset: 0;
    display: flex;
    align-items: center;
    justify-content: center;
    gap: 14px;
  }
  .brand__dot {
    width: 22px;
    height: 22px;
    border-radius: 50%;
    background: var(--mint);
    flex: none;
  }
  .brand__name {
    font-family: "Roboto", sans-serif;
    font-weight: 400;
    color: var(--mint);
    font-size: 28px;
    line-height: 34px;
    letter-spacing: 0;
  }

  /* Back: contact details */
  .contact {
    font-family: "Roboto", sans-serif;
    color: var(--ink);
  }
  .contact__name {
    position: absolute;
    left: 31px;
    top: 108px;
    font-size: 16.5px;
    font-weight: 700;
  }
  .contact__rule {
    position: absolute;
    left: 31px;
    top: 128px;
    width: 409px;
    height: 1.5px;
    background: var(--rule);
  }
  .contact__role {
    position: absolute;
    left: 31px;
    top: 131px;
    font-size: 12px;
  }
  .contact__line {
    position: absolute;
    left: 31px;
    display: flex;
    align-items: center;
    gap: 11px;
    font-size: 12.5px;
    white-space: nowrap;
  }
  .contact__line svg { width: 14px; height: 14px; flex: none; }
  .contact__line--web { top: 169px; }
  .contact__line--mail { top: 192px; }

  .band {
    position: absolute;
    left: 0;
    bottom: 0;
    width: 473px;
    height: 46px;
    background: var(--band);
  }
  .contact__line--phone {
    top: 229px;
    color: var(--band-text);
    font-weight: 500;
  }
</style>
</head>
<body>
<main class="canvas">
  <section class="card card--front">
    <div class="brand">
      <div class="brand__dot" aria-hidden="true"></div>
      <h1 class="brand__name">Marta Quinlan Photography</h1>
    </div>
  </section>

  <section class="card card--back contact">
    <h2 class="contact__name">Marta Quinlan</h2>
    <div class="contact__rule"></div>
    <p class="contact__role">Photographer</p>

    <p class="contact__line contact__line--web">
      <svg viewBox="0 0 14 14" aria-hidden="true" fill="none" stroke="#1c1c1c" stroke-width="1.1">
        <circle cx="7" cy="7" r="6"/>
        <ellipse cx="7" cy="7" rx="2.6" ry="6"/>
        <line x1="1" y1="7" x2="13" y2="7"/>
      </svg>
      www.pagerly.net/MartaQuinlanPhotography.Aust
    </p>
    <p class="contact__line contact__line--mail">
      <svg viewBox="0 0 14 14" aria-hidden="true">
        <rect x="0.5" y="2.5" width="13" height="9" fill="#1c1c1c"/>
        <path d="M0.5 2.8 7 8 13.5 2.8" fill="none" stroke="#ffffff" stroke-width="1"/>
      </svg>
      MartaQuinlanPhotography@brivomail.net
    </p>

    <div class="band" aria-hidden="true"></div>

    <p class="contact__line contact__line--phone">
      <svg viewBox="0 0 14 14" aria-hidden="true">
        <path d="M3 1.2 5.2 3.6 4 5.2c.8 1.9 2.3 3.4 4.2 4.4l1.5-1.2 2.5 2.1-1.4 2.1C6 12.4 1.6 8 1 2.7z" fill="#ffffff"/>
      </svg>
      0439 271 504
    </p>
  </section>
</main>
</body>
</html>
```